New Wine Label - Argentinian Malbec 'Viento Callado'

I am looking for an exceptional and exciting design for a wine label called 'Viento Callado' meaning Quiet Wind or Wind of the Quiet. The design must feature the name 'Viento Callado', a star logo and the word 'Malbec'. It will also need the words 'Mendoza, Argentina' at the bottom of the label as a prominent piece of information. Please produce the work in size 80mm x 100mm. Feel free to use colour in addition to black/white and ensue that the label is easy to read on a shelf placement.

Target Market(s)

25-50 Year Olds who enjoy great wine that looks and appears interesting and a little different.

Requirements
Must have
• Star Logo
• Word - Malbec
• Words - Mendoza, Argentina
Nice to have
• Background image to label

```html
<!DOCTYPE html>
<html lang="es">
<head>
<meta charset="utf-8">
<title>Viento Callado Malbec – Wine Label</title>
<link rel="stylesheet" href="https://fonts.googleapis.com/css2?family=Great+Vibes&display=swap">
<style>
  :root {
    --night-deep: #050506;
    --night-mid: #1b1d1f;
    --night-glow: #4a4f51;
    --gold: #c9a45a;
    --gold-light: #f1d79a;
    --gold-dark: #8a6a2c;
    --ivory: #ffffff;
  }
  html, body {
    margin: 0;
    padding: 0;
    width: 960px;
    height: 1200px;
    overflow: hidden;
    background: var(--night-deep);
  }
  .label {
    position: relative;
    width: 960px;
    height: 1200px;
    overflow: hidden;
    background: radial-gradient(ellipse 62% 48% at 50% 38%, var(--night-glow) 0%, var(--night-mid) 55%, var(--night-deep) 100%);
    font-family: "Great Vibes", cursive;
  }
  .shooting-star {
    position: absolute;
    left: 329px;
    top: 35px;
    width: 280px;
    height: 280px;
    background: radial-gradient(circle closest-side at 50% 50%, rgba(241, 215, 154, 0.5) 0%, rgba(201, 164, 90, 0.2) 40%, rgba(201, 164, 90, 0.06) 70%, rgba(201, 164, 90, 0) 100%);
  }
  .brand-name {
    position: absolute;
    top: 272px;
    left: 0;
    width: 960px;
    margin: 0;
    text-align: center;
    font-weight: 400;
    font-size: 92px;
    line-height: 1;
    color: var(--gold);
  }
  .varietal {
    position: absolute;
    top: 488px;
    left: 0;
    width: 960px;
    margin: 0;
    text-align: center;
    font-weight: 400;
    font-size: 134px;
    line-height: 1;
    color: var(--ivory);
    text-shadow: 3px 4px 4px rgba(0, 0, 0, 0.75);
  }
  .star-field {
    position: absolute;
    left: 0;
    top: 720px;
    width: 960px;
    height: 480px;
    background: linear-gradient(to bottom, rgba(201, 164, 90, 0) 0%, rgba(201, 164, 90, 0.08) 45%, rgba(201, 164, 90, 0.2) 100%);
  }
  .origin-band {
    position: absolute;
    left: 0;
    top: 1064px;
    width: 960px;
    height: 68px;
    background: var(--night-deep);
    border-top: 2px solid var(--gold);
    border-bottom: 2px solid var(--gold);
  }
  .origin {
    position: absolute;
    top: 1056px;
    left: 0;
    width: 960px;
    margin: 0;
    text-align: center;
    font-weight: 400;
    font-size: 74px;
    line-height: 1;
    color: var(--gold-light);
  }
</style>
</head>
<body>
  <main class="label">
    <div class="shooting-star" role="img" aria-label="Golden shooting star with a thin trail and sparkles"></div>
    <h1 class="brand-name">Viento Callado</h1>
    <h2 class="varietal">Malbec</h2>
    <div class="star-field" role="img" aria-label="Scattered small gold and ivory stars rising from the bottom edge"></div>
    <div class="origin-band"></div>
    <p class="origin">Mendoza, Argentina</p>
  </main>
</body>
</html>
```